EPS Recycling Rpt

Our annual recycling rate report needs a tune up. Our organization helps faciltate expanded polystyrene (EPS) recycling and this 4-page report highlights growth trends and useful information to help readers understand the dynamics of EPS recycling. We need a designer that can recreate the brochure we've published over the past several years with some minor adjustments to accomodate new content.

A PDF of the 2012 report is attached. Header text should reflect 2013 in all cases. Please pay close attention to the new placement of the copy as indicated in the Word file (also attached) as it has been significantly modified from the 2012 version. The color pallette for our branding is provided. Contact us with any questions.

```html
<!DOCTYPE html>
<html lang="en">
<head>
<meta charset="utf-8">
<title>2013 EPS Recycling Rate Report</title>
<link href="https://fonts.googleapis.com/css2?family=Ubuntu:wght@300;400;500;700&family=Ubuntu+Condensed&display=swap" rel="stylesheet">
<style>
:root{
  --band-dark:#3b3b3b;
  --paper:#ffffff;
  --steel-blue:#5d8aa6;
  --olive:#8f9a2b;
  --olive-circle:#a1a636;
  --orange:#f4a21f;
  --ink:#1e1e1e;
  --grid:#b9b9b9;
  --line-blue:#4a78b5;
  --condensed:"Ubuntu Condensed","Arial Narrow","Roboto Condensed",sans-serif;
}
*{margin:0;padding:0;box-sizing:border-box}
html,body{width:1200px;height:900px;overflow:hidden;background:var(--band-dark)}
.spread{position:relative;width:1200px;height:900px;overflow:hidden;
  background:radial-gradient(circle at 30% 40%,#4a4a4a,#2e2e2e)}
.page{position:absolute;left:0;top:65px;width:1200px;height:775px;background:var(--paper);overflow:hidden}
.title-band{position:absolute;left:0;top:0;width:1200px;height:115px;background:var(--steel-blue)}
.report-title{position:absolute;left:36px;top:20px;color:#fff;font:300 33px/1.18 "Ubuntu",sans-serif;letter-spacing:.3px}
.pellet-field{position:absolute;left:110px;top:130px;width:560px;height:540px;border-radius:50%;
  background:radial-gradient(ellipse at center,#e6e6e6 0%,#f0f0f0 45%,rgba(255,255,255,0) 72%)}
.section-head{position:absolute;left:36px;font:400 21px/1 "Ubuntu",sans-serif;color:var(--olive);z-index:2}
.section-head.blue{color:var(--steel-blue)}
.body-copy,.feature-copy{position:absolute;font-family:var(--condensed);font-size:8.6px;line-height:1.36;
  letter-spacing:-.2px;font-stretch:condensed;color:var(--ink);text-align:justify;z-index:2}
.criteria-copy{color:var(--steel-blue)}
.chart-caption{position:absolute;left:36px;top:229px;font:400 9px/1 var(--condensed);color:var(--ink)}
.rate-chart{position:absolute;left:30px;top:255px}
.collection-circle{position:absolute;left:595px;top:-435px;width:640px;height:640px;border-radius:50%;background:var(--olive-circle)}
.collection-head{position:absolute;left:664px;top:18px;font:400 21px/1 "Ubuntu",sans-serif;color:#fff;z-index:2}
.collection-copy{position:absolute;left:664px;top:47px;width:470px;font-family:var(--condensed);font-size:8.2px;line-height:1.4;
  letter-spacing:-.2px;font-stretch:condensed;font-weight:500;color:#fff;text-align:justify;z-index:2}
.photo{position:absolute;border-radius:50%;z-index:1}
.photo-volunteers{left:657px;top:157px;width:236px;height:236px;background:radial-gradient(circle at 50% 40%,#8a8070,#3c342c)}
.photo-unloading{left:875px;top:139px;width:186px;height:186px;background:radial-gradient(circle at 50% 45%,#9aa0a0,#3c3f3a)}
.photo-glue{left:835px;top:460px;width:170px;height:170px;background:radial-gradient(circle at 45% 50%,#6f8a4a,#26301e)}
.photo-surf{left:1005px;top:405px;width:195px;height:195px;background:radial-gradient(circle at 50% 45%,#e8e8e4,#9a9d98)}
.photo-plates{left:922px;top:585px;width:185px;height:185px;background:radial-gradient(circle at 55% 55%,#d8d6ce,#5a5852)}
.successes{position:absolute;left:730px;top:590px;width:180px;height:180px;border-radius:50%;background:var(--orange);
  color:#fff;text-align:center;padding-top:22px;z-index:3}
.successes h3{font:700 14px/1.2 var(--condensed)}
.successes ul{list-style:none;margin-top:9px;font:400 10.5px/1.37 var(--condensed)}
.social-circle{position:absolute;left:1035px;top:620px;width:170px;height:170px;border-radius:50%;background:var(--olive-circle);
  color:#fff;font:400 10.5px/1 var(--condensed);display:flex;align-items:center;justify-content:center;z-index:3}
</style>
</head>
<body>
<div class="spread">
  <div class="page">
    <div class="title-band"></div>
    <h1 class="report-title">2013 EPS RECYCLING<br>RATE REPORT</h1>

    <div class="pellet-field" role="img" aria-label="Pile of white recycled EPS foam pellets"></div>

    <h2 class="section-head" style="top:131px">EPS RECYCLING: Stronger Than Ever</h2>
    <p class="body-copy" style="left:36px;top:160px;width:555px">As shown in Figure 2, the EPS packaging recycling rate percentage continues to grow steadily, showing a dependable track record to deliver consistent results. In fact, when comparing rigid, durable PS and other grade materials, EPS post-consumer and post-commercial recycling represent 47% of all post-use polystyrene recycled in the U.S. and is one of the highest within the plastics family.</p>

    <p class="chart-caption">Figure 2: Post-Consumer EPS Recycling Rate History (1990-2013)</p>
    <svg class="rate-chart" width="500" height="130" viewBox="0 0 500 130" aria-label="Line chart of post-consumer EPS recycling rate, rising from about 2 percent in 1990 to 34 percent in 2013">
      <g stroke="var(--grid)" stroke-width="1">
        <line x1="32" y1="9" x2="485" y2="9"/><line x1="32" y1="35" x2="485" y2="35"/>
        <line x1="32" y1="60" x2="485" y2="60"/><line x1="32" y1="85" x2="485" y2="85"/>
        <line x1="32" y1="111" x2="485" y2="111"/>
      </g>
      <g font-family="Ubuntu, sans-serif" font-size="10" fill="#333" text-anchor="end">
        <text x="20" y="13">40</text><text x="20" y="39">30</text><text x="20" y="64">20</text><text x="20" y="89">10</text><text x="20" y="115">0</text>
      </g>
      <g font-family="Ubuntu, sans-serif" font-size="10" fill="#333" text-anchor="middle">
        <text x="48" y="128">1990</text><text x="84" y="128">1992</text><text x="117" y="128">1994</text><text x="152" y="128">1996</text><text x="187" y="128">1998</text><text x="222" y="128">2000</text><text x="257" y="128">2002</text><text x="290" y="128">2004</text><text x="325" y="128">2006</text><text x="361" y="128">2008</text><text x="396" y="128">2010</text><text x="431" y="128">2012</text><text x="467" y="128">2013</text>
      </g>
      <polyline fill="none" stroke="var(--line-blue)" stroke-width="2" points="48,107 84,87 117,86 152,84 187,88 222,80 257,78 290,80 325,63 361,62 396,40 431,35 467,25"/>
      <g fill="var(--line-blue)">
        <path d="M48 104l3 3-3 3-3-3z"/><path d="M84 84l3 3-3 3-3-3z"/><path d="M117 83l3 3-3 3-3-3z"/><path d="M152 81l3 3-3 3-3-3z"/><path d="M187 85l3 3-3 3-3-3z"/><path d="M222 77l3 3-3 3-3-3z"/><path d="M257 75l3 3-3 3-3-3z"/><path d="M290 77l3 3-3 3-3-3z"/><path d="M325 60l3 3-3 3-3-3z"/><path d="M361 59l3 3-3 3-3-3z"/><path d="M396 37l3 3-3 3-3-3z"/><path d="M431 32l3 3-3 3-3-3z"/><path d="M467 22l3 3-3 3-3-3z"/>
      </g>
    </svg>

    <h2 class="section-head" style="top:436px">Report Methodology</h2>
    <p class="body-copy" style="left:36px;top:467px;width:264px">The methodology for this annual report focuses on the development of a numerator and denominator figure. Recycled pounds, used as the numerator in the recycling rate equation, are based on an annual survey of post-consumer and post-commercial plastic recyclers (including EPS industry manufacturing facilities) and reflect the quantity of EPS recycled each year. Recycled pounds were counted at the stage where materials enter a reclamation facility (as opposed to net material recycled into resin or products) or were shipped for recycling outside the U.S.<br>Due to supply distribution chains and multiple end-use applications for EPS, a fixed number for EPS packaging generated each year is not availa-</p>
    <p class="body-copy" style="left:307px;top:467px;width:268px">ble. Other manufacturing streams include building and construction applications, sporting goods and other durable products. As a proxy, resin sales data as reported for custom molded applications are used as the denominator in the recycling rate equations, which were provided by the Resin Producers Statistics Council (RPSC). RPSC reports are compiled from primary data reported by resin producers to the professional services firm of Meridian Analytics, LLC. This does not account for non-U.S. resin sales which may offset the quantities reported by U.S. resin suppliers sold into custom molding facilities for non-packaging applications.</p>

    <h2 class="section-head blue" style="top:620px">Recycling Criteria</h2>
    <p class="body-copy criteria-copy" style="left:36px;top:652px;width:555px">Not all materials are well suited for recycling. Post-consumer EPS packaging must be clean and free of tape, film and cardboard. Expanded polystyrene made with a fire retardant additive, typically used in the manufacture of EPS building insulation, requires special reprocessing conditions. To enhance collection efforts and maximize the investment in recycling equipment, FRA recycling locations concentrate on large volume, commercial sources of post-consumer EPS. Some locations also offer consumer drop-off access.</p>
    <p class="body-copy criteria-copy" style="left:36px;top:711px;width:555px">To find out if EPS recycling is available in your area, visit www.foamrecovery.org. For consumers that do not have access to a local drop-off center, the Network of Foam Packaging Recyclers sponsors a National Take-Back Program intended for smaller quantities of EPS which can be mailed via the national postal service or ParcelGo to more than 30 locations nationwide. Full instructions and a list of Take-Back locations are available on the FRA website</p>

    <div class="collection-circle"></div>
    <h2 class="collection-head">PS Collection &amp; Reuse</h2>
    <p class="collection-copy">Expanded polystyrene (EPS) foam packaging is an excellent material for recycling and reuse with a 15 year history of environmental stewardship. Members of the Foam Recovery Alliance sponsor these efforts with ongoing financial support and active involvement in the collection and reprocessing of EPS. Recycling gives everybody a sense of well being. Working together with communities, local businesses and citizens, this unified approach is achieving increased awareness with bigger and better results – for a material often thought to be non-recyclable! Individually, none of these groups could have realized this exponential growth trend.</p>

    <div class="photo photo-volunteers" role="img" aria-label="Photo of volunteers in safety vests collecting foam in a truck"></div>
    <div class="photo photo-unloading" role="img" aria-label="Photo of residents unloading foam packaging from a car"></div>

    <p class="feature-copy" style="left:664px;top:388px;width:215px">While EPS is usually recycled into products such as coat hangers, insulation, decorative moldings and picture frames, new market developments continue to evolve. Ember Craft Products launched a new recycled glue product, Bondix, which is made from a blend of recycled polystyrene waste collected in the San Francisco Bay area and plant-based ingredients. This type of new and inventive market development is a key aspect of sustainable EPS recycling initiatives.</p>
    <p class="feature-copy" style="left:951px;top:333px;width:225px">For a fun and unique solution to EPS recycling, Foam-To-Surf collects material to make new surfboard blanks. With 18 collection sites in California, special events and corporate partnerships with Northridge Outfitters, Tidebreak and others, this initiative delivers a closed loop recycling solution and is spreading the word on surfing sustainability</p>

    <div class="photo photo-surf" role="img" aria-label="Photo of children beside a van with surfboard blanks"></div>
    <div class="photo photo-glue" role="img" aria-label="Photo of recycled glue bottle and jar"></div>
    <div class="photo photo-plates" role="img" aria-label="Photo of stacked white foam surfboard blanks"></div>

    <div class="successes">
      <h3>Other EPS<br>Recycling Successes:</h3>
      <ul>
        <li>NutriPath</li><li>Prairie Steaks</li><li>ValueMart</li><li>City of Harborton</li><li>Cyclone Appliance Corp.</li><li>City of Lakeview</li>
      </ul>
    </div>
    <div class="social-circle">social: /FoamRecovery</div>
  </div>
</div>
</body>
</html>
```